I need a business card for ALVA Holdings. We are a young startup based in New Zealand working in internet marketing and web development. The design should have some element connected to New Zealand, such as wave, koru or silver fern, just don't use a kiwi bird.

```html
<!DOCTYPE html>
<html lang="en">
<head>
<meta charset="utf-8">
<title>ALVA Holdings – Business Card</title>
<link href="https://fonts.googleapis.com/css2?family=Poppins:wght@400;500&display=swap" rel="stylesheet">
<style>
  :root {
    --backdrop: #d8d9db;
    --paper: #f4f4f4;
    --brand-blue: #0b6db5;
    --brand-orange: #ef5a24;
    --ink-grey: #5c5c5e;
  }
  * { margin: 0; padding: 0; box-sizing: border-box; }
  html, body {
    width: 1035px; height: 1200px; overflow: hidden;
    background: var(--backdrop);
    font-family: "Poppins", sans-serif;
  }
  .card {
    position: absolute; left: 91px; width: 847px; height: 484px;
    background: var(--paper);
  }
  .card--front { top: 95px; }
  .card--back { top: 631px; }
  .band {
    position: absolute; left: 102px; width: 641px; height: 15px;
  }
  .band--top { top: 0; background: var(--brand-orange); }
  .band--bottom { bottom: 0; background: var(--brand-blue); }

  .wordmark {
    position: absolute; left: 0; right: 0; top: 140px;
    text-align: center; color: var(--brand-blue); font-weight: 500;
  }
  .wordmark__main { display: block; font-size: 172px; line-height: 1; letter-spacing: 4px; }
  .wordmark__sub { display: block; font-size: 44px; line-height: 1; letter-spacing: 31px; margin-top: 16px; padding-left: 31px; }

  .mark {
    position: absolute; left: 96px; top: 122px; width: 178px; text-align: center;
    color: var(--brand-blue); font-weight: 500;
  }
  .mark__dot { display: block; width: 150px; height: 150px; margin: 0 auto; border-radius: 50%; background: var(--brand-blue); }
  .mark__name { display: block; margin-top: 14px; font-size: 22px; line-height: 1; }

  .contact { position: absolute; left: 316px; top: 120px; color: var(--ink-grey); }
  .contact__name { font-size: 37px; font-weight: 500; line-height: 1; }
  .contact__role { font-size: 22px; font-weight: 500; }
  .contact__list { list-style: none; margin-top: 12px; }
  .contact__item {
    position: relative; padding-left: 42px; font-size: 26px; letter-spacing: 1px;
    line-height: 40px;
  }
  .contact__icon { position: absolute; left: 0; top: 10px; width: 22px; height: 22px; }
  .contact__icon path, .contact__icon circle, .contact__icon rect {
    fill: none; stroke: var(--ink-grey); stroke-width: 1.5;
  }
</style>
</head>
<body>
  <section class="card card--front">
    <div class="band band--top"></div>
    <h1 class="wordmark">
      <span class="wordmark__main">ALVA</span>
      <span class="wordmark__sub">HOLDINGS</span>
    </h1>
    <div class="band band--bottom"></div>
  </section>

  <section class="card card--back">
    <div class="band band--top"></div>
    <div class="mark">
      <span class="mark__dot"></span>
      <span class="mark__name">ALVA Holdings</span>
    </div>
    <div class="contact">
      <p class="contact__name">Name Here <span class="contact__role">(Designation)</span></p>
      <ul class="contact__list">
        <li class="contact__item">
          <svg class="contact__icon" viewBox="0 0 22 22"><path d="M5 2l4 4-2 3c1 3 3 5 6 6l3-2 4 4-3 3C9 19 3 13 2 5z"/></svg>
          +0123456789
        </li>
        <li class="contact__item">
          <svg class="contact__icon" viewBox="0 0 22 22"><rect x="1" y="5" width="20" height="13"/><path d="M1 5l10 8 10-8M1 18l7-6M21 18l-7-6"/></svg>
          info@alvaholdings.com
        </li>
        <li class="contact__item">
          <svg class="contact__icon" viewBox="0 0 22 22"><circle cx="11" cy="11" r="9.5"/><path d="M4 7c3 0 4 2 3 4s1 4 3 5M14 3c-1 2 0 4 2 4s3 2 3 4M12 20c0-3 2-4 4-4"/></svg>
          www.alvaholdings.com
        </li>
        <li class="contact__item">
          <svg class="contact__icon" viewBox="0 0 22 22"><path d="M11 21S4 13 4 8a7 7 0 0 1 14 0c0 5-7 13-7 13z"/><circle cx="11" cy="8" r="2.5"/></svg>
          Road Name, Doar no.123<br>Building Name, State_0001
        </li>
      </ul>
    </div>
    <div class="band band--bottom"></div>
  </section>
</body>
</html>
```